Boutique Film/TV Company needs Business Card Design

Please see our website for background on our company and look of our current logo: www.morlandpictures.ca

Pantone 314U is our main colour.

Target Market(s)

Network of peers, funders and broadcasters.

Industry/Entity Type

Business

Requirements
Must have
• We would like rounded corners and the height of the card to be shorter than traditional (maybe?!)

It's important that we have room for our office address, office number, cell number, email address, website, facebook and linked-in info (though not all of us have a linked-in account).

Would like the logo to keep the exclamation marks over the letters but the tag line/tag words of "film - television - interactive" can stay or go or... surprise me!

Nice to have
• Silky matte finish.

We are open to a change in the font of our logo/name.

```html
<!DOCTYPE html>
<html lang="en">
<head>
<meta charset="utf-8">
<title>Morland Business Card</title>
<link rel="stylesheet" href="https://fonts.googleapis.com/css2?family=Source+Sans+3:wght@400;600;700&display=swap">
<style>
  :root {
    --bg: #e9e6e2;
    --card-white: #ffffff;
    --brand-blue: #0b86ae;
    --brand-red: #9b1b20;
    --ink: #111111;
    --text: #3b3b3b;
    --social-one: #3b6fb6;
    --social-two: #2f5d3a;
  }
  * { box-sizing: border-box; margin: 0; padding: 0; }
  html, body { width: 960px; height: 1200px; overflow: hidden; }
  body {
    position: relative;
    background: var(--bg);
    font-family: "Source Sans 3", "Helvetica Neue", Arial, sans-serif;
    color: var(--text);
  }
  .card {
    position: absolute;
    width: 840px;
    height: 479px;
    border-radius: 30px;
    overflow: hidden;
    box-shadow: 4px 6px 10px rgba(0,0,0,0.25);
  }
  .card--front { left: 60px; top: 48px; background: var(--card-white); }
  .card--back { left: 55px; top: 638px; background: var(--brand-blue); }

  .brand-name {
    position: absolute;
    left: 0; right: 0;
    text-align: center;
    font-weight: 600;
    font-size: 104px;
    line-height: 1;
    letter-spacing: -1px;
  }
  .card--front .brand-name { top: 72px; color: var(--ink); }
  .card--back .brand-name { top: 150px; color: var(--card-white); font-size: 112px; }

  .tagline {
    position: absolute;
    left: 0; right: 0;
    text-align: center;
    font-weight: 700;
    font-size: 21px;
    letter-spacing: 0.2px;
  }
  .card--front .tagline { top: 197px; color: var(--brand-red); }
  .card--front .tagline .sep { color: var(--ink); }
  .card--back .tagline { top: 315px; color: var(--card-white); font-size: 24px; }

  .contact-line {
    position: absolute;
    left: 0; right: 0;
    text-align: center;
    font-size: 20px;
  }
  .contact-name { top: 238px; font-size: 20px; }
  .contact-name strong { font-size: 25px; font-weight: 700; }
  .contact-phone { top: 284px; }
  .contact-web { top: 325px; }
  .contact-line em { font-weight: 700; font-style: italic; }
  .contact-line .divider { padding: 0 8px; }

  .social {
    position: absolute;
    top: 372px; left: 0; right: 0;
    display: flex; justify-content: center; align-items: center; gap: 8px;
    font-weight: 700; font-size: 21px;
  }
  .social-mark { width: 31px; height: 31px; border-radius: 3px; }
  .social-mark--one { background: var(--social-one); margin-left: 4px; }
  .social-mark--two { background: var(--social-two); }

  .rule-red {
    position: absolute; left: 0; right: 0; top: 410px;
    height: 4px; background: var(--brand-red);
  }
  .address-band {
    position: absolute; left: 0; right: 0; top: 417px; bottom: 0;
    background: var(--brand-blue);
    border-top: 2px solid var(--card-white);
    color: var(--card-white);
    font-size: 25px;
    text-align: center;
    line-height: 60px;
  }
</style>
</head>
<body>
  <section class="card card--front">
    <div class="brand-name">Morland</div>
    <div class="tagline">Films <span class="sep">•</span> Television <span class="sep">•</span> Interactive</div>
    <div class="contact-line contact-name"><strong>Your Name -</strong> Designation</div>
    <div class="contact-line contact-phone"><em>t</em> : 416.555.0192<span class="divider">|</span><em>c</em> : 123.123.1234</div>
    <div class="contact-line contact-web"><em>e</em> : info@morlandpictures.ca<span class="divider">|</span><em>w</em> : www.morlandpictures.ca</div>
    <div class="social">Follow <span class="social-mark social-mark--one"></span><span class="social-mark social-mark--two"></span></div>
    <div class="rule-red"></div>
    <div class="address-band">42 Larkin Avenue, Toronto, ON M4E 2K8</div>
  </section>

  <section class="card card--back">
    <div class="brand-name">Morland</div>
    <div class="tagline">Films • Television • Interactive</div>
  </section>
</body>
</html>
```